Fashion Wholesale Product Page

We need a product page layout for a wholesale catalogue.
It will include a title, 3 images, short description, prices and size and colour options in an a5 page for print.
We'd like a design file that we can use to update with new products in the future.
All images and content will be provided.
The range we are selling is all about simplicity and minimalism so we'd love this to be reflected in the layout.

Target Market(s)

Young, fashion conscious women with a strong appreciation for good, simple design.

Industry/Entity Type

Fashion

Requirements
Must have
• Title - 'Wren Bodice'
Short Description - 'Perfect for a smaller bust, the wren bodice is divine simplicity. Featuring our well known triangle cut and darted cups, we have perfected this design for an optimal fit.'
Prices - Wholesale: $30 RRP: $60
Available in -
Colours Black, White, Grey Marle
Sizes XS, S, M, L

3 product images
Nice to have
• If it fits with the design it would be great to include the image on the model attached here.

I don't want it to feel too crowded though.

```html
<!DOCTYPE html>
<html lang="en">
<head>
<meta charset="utf-8">
<title>Wholesale Catalogue Spread</title>
<link rel="stylesheet" href="https://fonts.googleapis.com/css2?family=Didact+Gothic&family=Questrial&display=swap">
<style>
  :root {
    --backdrop: #e8e5e1;
    --paper: #ffffff;
    --ink: #2b2b2b;
    --ink-soft: #5a5a5a;
    --accent-red: #c8262c;
    --rule-grey: #b9b9b9;
    --photo-grey: #d9d6d3;
    --studio-red: #a8182a;
  }
  * { margin: 0; padding: 0; box-sizing: border-box; }
  html, body { width: 1200px; height: 829px; overflow: hidden; }
  body { background: var(--backdrop); position: relative; font-family: "Didact Gothic", sans-serif; color: var(--ink); }

  .spread { position: absolute; left: 165px; top: 88px; width: 845px; height: 622px; display: flex; box-shadow: 0 6px 24px rgba(0,0,0,.18); }
  .page { position: relative; width: 50%; height: 100%; background: var(--paper); overflow: hidden; }
  .page--left { background: linear-gradient(to left, #e9e9e9 0, var(--paper) 18px); }
  .page--right { background: linear-gradient(to right, #e9e9e9 0, var(--paper) 18px); }

  .photo { position: absolute; }
  .model-shot { left: 8px; top: 9px; width: 186px; height: 308px; background: linear-gradient(180deg, #e4e1de 0%, var(--photo-grey) 60%, #cfccc9 100%); }
  .model-shot-bar { position: absolute; left: 8px; top: 312px; width: 186px; height: 6px; background: var(--accent-red); }

  .product-title { position: absolute; font-family: "Questrial", sans-serif; font-weight: 400; font-size: 27px; line-height: 34px; letter-spacing: 0.5px; color: var(--ink); }
  .product-title span { display: inline-block; border-bottom: 4px solid var(--accent-red); padding-bottom: 0; line-height: 28px; margin-bottom: 6px; }

  .description { position: absolute; font-size: 12.5px; line-height: 17px; color: var(--ink-soft); }
  .description p + p { margin-top: 15px; }

  .rule { position: absolute; height: 2px; background: var(--rule-grey); }

  .specs { position: absolute; font-size: 12.5px; line-height: 20px; color: var(--ink-soft); }
  .specs dt { display: inline; color: var(--ink); }
  .specs dd { display: inline; }

  .folio { position: absolute; bottom: 8px; font-size: 11px; color: var(--ink-soft); }
  .brand-mark { position: absolute; bottom: 6px; font-family: "Questrial", sans-serif; font-size: 12px; letter-spacing: 1px; color: var(--ink); }

  .left .product-title { left: 207px; top: 28px; }
  .left .description { left: 207px; top: 128px; width: 200px; }
  .left .rule { left: 207px; top: 250px; width: 200px; }
  .left .specs { left: 207px; top: 256px; width: 215px; }

  .flat-white { left: 35px; top: 365px; width: 140px; height: 112px; background: linear-gradient(160deg, #f4f4f4, #e3e3e3); border-radius: 4px 4px 40px 40px; }
  .flat-black { left: 255px; top: 357px; width: 145px; height: 130px; background: linear-gradient(160deg, #2a2a2a, #111); border-radius: 4px 4px 40px 40px; }
  .flat-grey  { left: 150px; top: 487px; width: 135px; height: 116px; background: linear-gradient(160deg, #c9c9c9, #a9a9a9); border-radius: 4px 4px 40px 40px; }

  .right .product-title { left: 25px; top: 18px; }
  .right .description { left: 25px; top: 125px; width: 210px; }
  .bra-flat { left: 25px; top: 367px; width: 180px; height: 150px; background: linear-gradient(90deg, #1d1f26 0%, #1d1f26 22%, #f1ece6 35%, #f1ece6 78%, #1d1f26 90%); border-radius: 6px; }
  .right .specs { left: 25px; top: 546px; width: 210px; }
  .studio-shot { right: 0; top: 0; width: 188px; height: 100%; background: linear-gradient(180deg, #b51c2e 0%, var(--studio-red) 55%, #8f1422 100%); }
</style>
</head>
<body>
  <main class="spread">
    <section class="page page--left left">
      <div class="photo model-shot" role="img" aria-label="Model wearing the grey marle high waisted brief and matching bra"></div>
      <div class="model-shot-bar"></div>

      <h2 class="product-title"><span>HIGH WAISTED</span><br><span>BRIEF</span></h2>
      <div class="description">
        <p>The high waisted brief is all about clean lines.</p>
        <p>Sitting comfortably on your waist, this piece has been skilfully cut with a panelled front for some subtle shaping.</p>
      </div>
      <div class="rule"></div>
      <dl class="specs">
        <div><dt>Prices</dt> <dd>Wholesale: $X0 RRP: $X0</dd></div>
        <div><dt>Colours</dt> <dd>Black, White, Grey Marle</dd></div>
        <div><dt>Sizes</dt> <dd>XS, S, M, L</dd></div>
      </dl>

      <div class="photo flat-white" role="img" aria-label="White high waisted brief, flat product shot"></div>
      <div class="photo flat-black" role="img" aria-label="Black high waisted brief, flat product shot"></div>
      <div class="photo flat-grey" role="img" aria-label="Grey marle high waisted brief, flat product shot"></div>

      <span class="folio" style="left:33px;">4</span>
      <span class="brand-mark" style="right:10px;">LUMA</span>
    </section>

    <section class="page page--right right">
      <h2 class="product-title"><span>THE KEYSTONE</span><br><span>BRA</span></h2>
      <div class="description">
        <p>Asymmetry with precision.</p>
        <p>A soft cup wren bodice with distinction.</p>
        <p>A composition of 3 front panels in luxe white bamboo jersey with a right side feature panel of black organic cotton/ bamboo velour and a midnight blue bamboo jersey back. A striking addition to your underwear drawer and an easy favourite of the collection.</p>
      </div>

      <div class="photo bra-flat" role="img" aria-label="Black and white panelled soft cup bra, flat product shot"></div>

      <dl class="specs">
        <div><dt>Prices</dt> <dd>Wholesale: $X0 RRP: $X0</dd></div>
        <div><dt>Colours</dt> <dd>Black, White, Grey Marle</dd></div>
        <div><dt>Sizes</dt> <dd>XS, S, M, L</dd></div>
      </dl>

      <div class="photo studio-shot" role="img" aria-label="Model standing against a red studio backdrop wearing the panelled bra and brief"></div>

      <span class="brand-mark" style="left:3px;">LUMA</span>
      <span class="folio" style="right:12px; color:#fff;">5</span>
    </section>
  </main>
</body>
</html>
```